Präsentationsvorlagen für Automotive Engineering
Zielgruppe
Automotive Engineering - Software & Embedded systems are main focus including V-Modell
Aufgabenstellung
see Logo

```html
<!DOCTYPE html>
<html lang="de">
<head>
<meta charset="utf-8">
<title>Präsentationsvorlagen – VORATEK</title>
<link href="https://fonts.googleapis.com/css2?family=Montserrat:ital,wght@0,300;0,400;0,600;0,700;1,300;1,400&display=swap" rel="stylesheet">
<style>
  :root {
    --navy: #0b2b59;
    --red: #e30613;
    --white: #ffffff;
    --paper: #ffffff;
  }
  * { margin: 0; padding: 0; box-sizing: border-box; }
  html, body {
    width: 1200px; height: 900px; overflow: hidden;
    background: var(--paper);
    font-family: "Montserrat", sans-serif;
    color: var(--white);
  }
  .sheet { position: relative; width: 1200px; height: 900px; }
  .slide {
    position: absolute; width: 520px; height: 390px;
    background: var(--navy);
    box-shadow: 0 0 14px rgba(0,0,0,0.22);
    overflow: hidden;
  }
  .slide--agenda  { left: 45px;  top: 42px; }
  .slide--content { left: 620px; top: 42px; }
  .slide--title   { left: 45px;  top: 461px; }
  .slide--closing { left: 620px; top: 461px; }

  .accent-bar { position: absolute; left: 0; width: 5px; background: var(--red); }
  .slide-heading {
    position: absolute; left: 65px; top: 38px;
    font-size: 26px; font-weight: 700; letter-spacing: 0.2px;
  }
  .footer-brand {
    position: absolute; left: 392px; top: 364px;
    font-size: 13px; font-weight: 700; letter-spacing: 1.5px;
  }
  .page-number {
    position: absolute; left: 481px; top: 356px; width: 39px; height: 34px;
    background: var(--red);
    font-size: 14px; font-weight: 700;
    display: flex; align-items: center; justify-content: center;
  }

  .agenda-list { position: absolute; left: 65px; top: 0; list-style: none; }
  .agenda-item { position: absolute; white-space: nowrap; }
  .agenda-item--main { font-size: 13px; font-weight: 700; left: 0; }
  .agenda-item--sub  { font-size: 13px; font-weight: 400; left: 20px; }

  .content-block { position: absolute; left: 64px; width: 360px; }
  .content-block h3 { font-size: 13px; font-weight: 700; margin-bottom: 10px; }
  .content-block p { font-size: 9px; line-height: 11.8px; font-weight: 400; }

  .brand-name { font-weight: 700; letter-spacing: 3px; }
  .slide--title .brand-name { position: absolute; left: 66px; top: 124px; font-size: 40px; }
  .presentation-title {
    position: absolute; left: 65px; top: 234px;
    font-size: 26px; font-weight: 700; white-space: nowrap;
  }
  .presentation-subtitle {
    position: absolute; left: 65px; top: 263px;
    font-size: 21px; font-weight: 300; font-style: italic;
  }
  .speaker {
    position: absolute; left: 68px; top: 298px;
    font-size: 12.5px; font-weight: 400; line-height: 16px;
  }

  .slide--closing .brand-name {
    position: absolute; left: 0; right: 0; top: 150px;
    text-align: center; font-size: 44px;
  }
  .closing-message {
    position: absolute; left: 0; right: 0; top: 263px;
    text-align: center; font-size: 21px; line-height: 27px;
  }
  .closing-message strong { font-weight: 700; display: block; }
  .closing-message span { font-weight: 300; display: block; }
</style>
</head>
<body>
<main class="sheet">

  <section class="slide slide--agenda">
    <div class="accent-bar" style="top:30px;height:51px"></div>
    <h2 class="slide-heading">AGENDA</h2>
    <ul class="agenda-list">
      <li class="agenda-item agenda-item--main" style="top:112px">Projektpunkt 1</li>
      <li class="agenda-item agenda-item--main" style="top:147px">Projektpunkt 2</li>
      <li class="agenda-item agenda-item--sub" style="top:171px">Projektunterpunkt 2.1</li>
      <li class="agenda-item agenda-item--sub" style="top:197px">Projektunterpunkt 2.2</li>
      <li class="agenda-item agenda-item--sub" style="top:222px">Projektunterpunkt 2.3</li>
      <li class="agenda-item agenda-item--main" style="top:254px">Projektpunkt 3</li>
      <li class="agenda-item agenda-item--sub" style="top:279px">Projektunterpunkt 3.1</li>
    </ul>
    <div class="footer-brand">VORATEK</div>
    <div class="page-number">01</div>
  </section>

  <section class="slide slide--content">
    <div class="accent-bar" style="top:30px;height:51px"></div>
    <h2 class="slide-heading">Projektpunkt 1</h2>
    <article class="content-block" style="top:122px">
      <h3>Überschrift</h3>
      <p>Lorem ipsum dolor sit amet, consectetuer adipiscing elit, sed diam no-<br>nummy nibh euismod tincidunt ut laoreet dolore magna aliquam erat<br>volutpat. Ut wisi enim ad minim veniam, quis nostrud exerci tation ull-</p>
    </article>
    <article class="content-block" style="top:210px">
      <h3>Überschrift</h3>
      <p>Lorem ipsum dolor sit amet, consectetuer adipiscing elit, sed diam no-<br>nummy nibh euismod tincidunt ut laoreet dolore magna aliquam erat<br>volutpat. Ut wisi enim ad minim veniam, quis nostrud exerci tation ull-</p>
    </article>
    <div class="footer-brand">VORATEK</div>
    <div class="page-number">01</div>
  </section>

  <section class="slide slide--title">
    <div class="brand-name">VORATEK</div>
    <div class="accent-bar" style="top:229px;height:111px"></div>
    <h1 class="presentation-title">Präsentationsthematik</h1>
    <p class="presentation-subtitle">Unterüberschrift</p>
    <p class="speaker">Redner:<br>Herr Max Mustermann</p>
  </section>

  <section class="slide slide--closing">
    <div class="brand-name">VORATEK</div>
    <p class="closing-message"><strong>Vielen Dank</strong><span>für Ihre Aufmerksamkeit</span></p>
  </section>

</main>
</body>
</html>
```